modern, IT themed business card for IT accelerator

Design a business card for tech oriented business accelerator. Prevailing color shall be orange.
we are operating in emerging markets and our mission is to provide co-working space, mentorship/coaching and ultimately seed financing IT startups.
also, we are helping financed ITs in obtaining next round financing, and to this end we are meeting with non IT/finance people and investment professionals..
that means card shall be designed to "impress" not only IT people (mostly liberal) but finance (more conservative)

Industry/Entity Type

Investment

Contact Information for Business Card

Company Name: Pelor Founders Yard
Name: Temur Kobaladze
Position: Partner
Address: 14, N Abashidze St., Tbilisi 0162, Georgia
Tel: +995599438165
Email: t.kobaladze@pelorhub.ge
Website: www.pelorhub.ge

Font styles to use
Sans Serif

Requirements
Must have
• Attached are logos of the company (portrait & landscape) choose any
Nice to have
• industry is IT and finance (in fact, financing IT startups). therefore design might have IT theme (inspiration from web or software designs)

```html
<!DOCTYPE html>
<html lang="en">
<head>
<meta charset="utf-8">
<title>Pelor Founders Yard – Business Card</title>
<link rel="stylesheet" href="https://fonts.googleapis.com/css2?family=Exo+2:wght@400;500;600;700&display=swap">
<style>
  :root {
    --page: #e6e6e4;
    --card: #f7f7f7;
    --card-shade: #e9e9e9;
    --band-top: #7c7c7c;
    --band-bottom: #a3a3a3;
    --orange: #f7931e;
    --orange-deep: #e87511;
    --ink: #4a4a4a;
    --ink-soft: #6b6b6b;
    --white: #ffffff;
  }
  * { margin: 0; padding: 0; box-sizing: border-box; }
  html, body {
    width: 1200px; height: 899px; overflow: hidden;
    background: var(--page);
    font-family: "Exo 2", sans-serif;
  }
  .card {
    position: absolute; left: 100px; top: 160px;
    width: 1000px; height: 580px;
    border-radius: 44px; overflow: hidden;
    background: radial-gradient(ellipse at 45% 60%, var(--white) 0%, var(--card) 45%, var(--card-shade) 100%);
    box-shadow: 0 14px 40px rgba(0,0,0,0.18);
  }
  .card-art { position: absolute; inset: 0; }
  .holder {
    position: absolute; right: 60px; top: 56px; text-align: right; color: var(--white);
  }
  .holder-name { font-size: 40px; font-weight: 600; letter-spacing: 2px; text-transform: uppercase; }
  .holder-role { font-size: 26px; font-weight: 500; margin-top: 6px; }
  .contacts {
    position: absolute; left: 44px; top: 360px; list-style: none;
    color: var(--ink-soft); font-size: 17px; font-weight: 500;
  }
  .contacts li { display: flex; align-items: center; height: 30px; gap: 12px; }
  .contacts svg { width: 16px; height: 16px; fill: var(--ink-soft); flex: none; }
  .brand {
    position: absolute; left: 440px; top: 320px;
    display: flex; align-items: center; gap: 18px;
  }
  .brand-dot {
    width: 62px; height: 62px; border-radius: 50%; background: var(--orange);
  }
  .brand-name {
    font-size: 44px; font-weight: 600; color: var(--ink); letter-spacing: 1px; line-height: 1;
  }
  .address {
    position: absolute; right: 60px; top: 470px; text-align: right;
    color: var(--ink); font-size: 19px; font-weight: 500; line-height: 1.35;
  }
</style>
</head>
<body>
  <section class="card">
    <svg class="card-art" viewBox="0 0 1000 580" preserveAspectRatio="none" aria-hidden="true">
      <defs>
        <linearGradient id="band" x1="0" y1="0" x2="0" y2="1">
          <stop offset="0" stop-color="var(--band-top)"/>
          <stop offset="1" stop-color="var(--band-bottom)"/>
        </linearGradient>
        <linearGradient id="swoosh" x1="0" y1="0" x2="1" y2="0">
          <stop offset="0" stop-color="var(--orange-deep)"/>
          <stop offset="0.5" stop-color="var(--orange)"/>
          <stop offset="1" stop-color="var(--orange-deep)"/>
        </linearGradient>
      </defs>
      <path class="top-band" d="M0 0 H1000 V330 C820 120 520 80 250 105 C140 115 60 140 0 170 Z" fill="url(#band)"/>
      <path class="orange-swoosh" d="M0 176 C70 142 150 120 260 110 C530 86 820 125 1000 338 L1000 360 C820 150 520 108 262 128 C150 138 70 160 0 196 Z" fill="url(#swoosh)"/>
    </svg>

    <div class="holder">
      <div class="holder-name">Temur Kobaladze</div>
      <div class="holder-role">Managing Director</div>
    </div>

    <ul class="contacts">
      <li><svg viewBox="0 0 16 16"><path d="M3 1l3 3-2 2c1 2 3 4 5 5l2-2 3 3-2 3C6 14 2 10 1 3z"/></svg>+995 599 438 165</li>
      <li><svg viewBox="0 0 16 16"><path d="M4 0h8v16H4zM5.5 2v10h5V2z"/></svg>+995 322 438 165</li>
      <li><svg viewBox="0 0 16 16"><path d="M4 1h7v4H4zM1 6h14v8H1zM4 10h8v5H4z"/></svg>+995 322 438 166</li>
      <li><svg viewBox="0 0 16 16"><path d="M1 3l7 5 7-5v10H1zM1 2h14L8 7z"/></svg>t.kobaladze@pelorhub.ge</li>
      <li><svg viewBox="0 0 16 16"><path d="M8 0a8 8 0 100 16A8 8 0 008 0zm0 2a6 6 0 110 12A6 6 0 018 2zM2 7h12v2H2zM7 2h2v12H7z"/></svg>www.pelorhub.ge</li>
    </ul>

    <div class="brand">
      <span class="brand-dot"></span>
      <span class="brand-name">Pelor Founders Yard</span>
    </div>

    <address class="address" style="font-style:normal">
      14, N Abashidze St.,<br>Tbilisi 0162, Georgia
    </address>
  </section>
</body>
</html>
```